Tequila Velmaros Web Design Project

We are launching a new Ultra Premium Tequila; the brand name is "Velmaros".
Velmaros was the colloquial name given to Spanish immigrants that came to America in the 19th and early part of the 20th centuries, made fortune and went back to Spain to propel even greater opportunities for those in their homeland, started banks, built schools, roads, built eclectic houses, some acquired noble titles, they were brazen, altruist and built a better world along the way.
Our product is 100% Blue Agave and will have the 4 types of tequila: Silver, Reposado, Añejo and Extra Añejo.
Updates

Dear All,
I have attached some more information/content for your review.
Kind Regards,

After some consideration, we have decided to include our line of Premium Margaritas on the same site.
Our Margaritas are made with 100% Blue Agave Silver Tequila and lightly sweetened with Agave Nectar.
Please see file with the 5 different flavors available.
Thank you,

Target Market(s)

Our target market is affluent people, especially Hispanics, because most of the have a Spanish heritage and/or ancestry; also, entrepreneurs of today.

Industry/Entity Type

Product

Requirements
Must have
• We will provide pictures and content/text for the pages.

```html
<!DOCTYPE html>
<html lang="en">
<head>
<meta charset="utf-8">
<title>Velmaros Tequila</title>
<link rel="stylesheet" href="https://fonts.googleapis.com/css2?family=Sorts+Mill+Goudy&family=PT+Sans:ital,wght@0,400;0,700;1,400&display=swap">
<style>
:root{
  --maroon:#5e1b1b;
  --maroon-light:#6e2222;
  --maroon-dark:#4a1313;
  --tab:#571616;
  --ink:#2b2b2b;
  --white:#ffffff;
  --grey-card:#e4e4e4;
  --title-red:#6a1d1d;
  --muted:#c9a9a9;
}
*{margin:0;padding:0;box-sizing:border-box}
html,body{width:697px;height:1200px;overflow:hidden;background:var(--white)}
body{font-family:"PT Sans",sans-serif;color:var(--white)}
.page{position:relative;width:697px;height:1200px;overflow:hidden}
.abs{position:absolute}

.top{left:0;top:0;width:697px;height:760px;background:linear-gradient(180deg,var(--maroon) 0%,var(--maroon-light) 45%,var(--maroon) 100%);border-top:3px solid #9c9c9c}
.utility{right:18px;top:10px;font-size:8px;color:#e6d3d3}
.utility span{margin:0 3px;color:#b88}
.brand{left:25px;top:24px;font-family:"Sorts Mill Goudy",serif;font-size:26px;color:var(--white);letter-spacing:.3px}
.slogan{left:36px;top:53px;font-size:8px;color:#ecdcdc}
.search{left:480px;top:54px;width:199px;height:18px;background:#e8e3e3;border:1px solid #bbb}
.search span{position:absolute;left:7px;top:3px;font-size:7.5px;font-style:italic;color:#777}
.search svg{position:absolute;right:4px;top:3px}

.nav{left:14px;top:85px;width:669px;height:38px;background:#0c0606;display:flex;align-items:center;padding-left:14px}
.nav a{color:var(--white);text-decoration:none;font-size:9px;padding:0 18px;border-right:1px solid #5a4a4a;line-height:15px}
.nav a:last-child{border-right:none}

.hero{left:15px;top:123px;width:667px;height:323px;border:2px solid var(--white);border-top:none;box-shadow:0 8px 10px rgba(0,0,0,.35);background:linear-gradient(100deg,#5a3a26 0%,#a88a6c 30%,#7a5236 55%,#9a7656 75%,#6e5a4c 100%)}
.hero-arrow{top:120px}
.caption{left:319px;top:162px;width:300px;height:108px;background:rgba(245,241,238,.96);padding:11px 16px;color:var(--title-red)}
.caption h2{font-family:"Sorts Mill Goudy",serif;font-weight:400;font-size:17.5px}
.caption h3{font-weight:400;font-size:9.5px;color:#6a1a1a;margin-top:3px}
.caption p{font-size:7.3px;line-height:12px;color:#7a2525;margin-top:4px}
.caption a{display:block;font-size:7.5px;font-weight:700;color:#3a1a1a;margin-top:5px;text-decoration:none}

.col{top:495px;width:200px;height:245px}
.col-head{height:27px;background:var(--tab);font-family:"Sorts Mill Goudy",serif;font-size:13px;padding:6px 9px;position:relative}
.col-head::after{content:"";position:absolute;right:18px;bottom:-5px;border-left:5px solid transparent;border-right:5px solid transparent;border-top:5px solid var(--tab)}
.col-photo{margin-top:10px;height:69px;border:2px solid #8a3a3a}
.col-lead{font-size:7.3px;font-weight:700;line-height:13px;margin-top:10px}
.col-body{font-size:7.3px;line-height:13px;text-align:justify;margin-top:6px;color:#f0e3e3}
.btn{display:inline-block;background:var(--white);color:#4a1a1a;font-size:8px;padding:2px 9px;text-decoration:none}
.post{position:absolute;left:1px;width:200px}
.post h4{font-size:8px;font-weight:700;line-height:10px}
.post p{font-size:7.3px;line-height:12.5px;color:#f0e3e3;margin-top:2px}
.post em{display:block;font-size:7px;line-height:9px;color:var(--muted);margin-top:3px}

.brands-title{left:40px;top:777px;font-family:"Sorts Mill Goudy",serif;font-size:13px;font-weight:400;color:var(--title-red)}
.card{width:113px;height:147px;background:var(--grey-card)}
.card .shot{position:absolute;left:5px;top:5px;width:103px;height:115px;background:radial-gradient(ellipse at 50% 58%,#d8d8d8 0%,#f4f4f4 35%,#ffffff 70%)}
.card .shot.dark{background:radial-gradient(ellipse at 50% 58%,#2a2a2a 0%,#6a6a6a 25%,#ffffff 55%)}
.card span{position:absolute;left:13px;top:126px;font-size:8.5px;color:var(--ink)}

.footer{left:0;top:1131px;width:697px;height:69px;background:linear-gradient(180deg,var(--maroon-dark),var(--maroon))}
.footer nav{position:absolute;left:21px;top:17px;font-size:7.8px}
.footer nav a{color:var(--white);text-decoration:none;margin-right:16px}
.footer small{position:absolute;left:21px;top:36px;font-size:7px;color:#d8c2c2}
.social{position:absolute;right:18px;top:17px;display:flex;gap:6px}
.social i{width:17px;height:17px;border-radius:50%;background:#8a6a6a;display:block}
</style>
</head>
<body>
<div class="page">
  <div class="abs top"></div>

  <div class="abs utility">FAQ<span>|</span>Support<span>|</span>Sitemap<span>|</span>Location<span>|</span>Partner</div>
  <div class="abs brand">Velmaros</div>
  <div class="abs slogan">your slogan goes here</div>
  <div class="abs search"><span>enter keyword</span>
    <svg width="12" height="12" viewBox="0 0 12 12"><circle cx="5" cy="5" r="3.6" fill="none" stroke="#2a2a2a" stroke-width="1.8"/><line x1="7.6" y1="7.6" x2="11" y2="11" stroke="#2a2a2a" stroke-width="2"/></svg>
  </div>

  <nav class="abs nav">
    <a href="#">COMPANY</a><a href="#">ABOUT US</a><a href="#">PRODUCTS</a><a href="#">MANUFACTURE</a><a href="#">BRANDS</a><a href="#">BLOG</a><a href="#">OUR PLANT</a><a href="#">CONTACT</a>
  </nav>

  <div class="abs hero" role="img" aria-label="Two master distillers inspecting a glass of tequila among oak barrels">
    <svg class="abs hero-arrow" style="left:10px" width="22" height="56" viewBox="0 0 22 56"><polyline points="20,2 2,28 20,54" fill="none" stroke="#1a1a1a" stroke-width="1.4"/></svg>
    <svg class="abs hero-arrow" style="right:10px" width="22" height="56" viewBox="0 0 22 56"><polyline points="2,2 20,28 2,54" fill="none" stroke="#1a1a1a" stroke-width="1.4"/></svg>
    <div class="abs caption">
      <h2>Velmaros punch line goes here</h2>
      <h3>Donec convallis pede venenatis nibh.</h3>
      <p>Lorem ipsum dolor sit amet, consectetuer adipiscing elit. Nam cursus. Morbi ut mi. Nullam enim leo, egestas id, condimentum.</p>
      <a href="#">LEARN MORE ›</a>
    </div>
  </div>

  <section class="abs col" style="left:16px">
    <div class="col-head">Our Mission</div>
    <div class="col-photo" role="img" aria-label="Distillery worker beside steel tanks" style="background:linear-gradient(90deg,#6a6a66,#b8b4ac 40%,#d8d4cc 70%,#8a8a86)"></div>
    <p class="col-lead">Lorem ipsum dolor sit amet, consectetuer adipiscing elit. Nam cursus.</p>
    <p class="col-body">Morbi ut mi. Nullam enim leo, egestas id, condimentum at, laoreet mattis, massa. Sed eleifend nonummy diam. Praesent mauris ante, elementum et, bibendum at, posuere sit amet, nibh. Duis tincidunt lectus quis dui viverra vestibulum. Suspendisse vulputate aliquam dui. Nulla elementum dui ut augue.</p>
    <a class="btn abs" href="#" style="left:-2px;top:228px">learn more ›</a>
  </section>

  <section class="abs col" style="left:244px">
    <div class="col-head">Manufacture &amp; Making</div>
    <div class="col-photo" role="img" aria-label="Harvester working in a blue agave field" style="background:linear-gradient(180deg,#1e2a22,#3c4a3e 50%,#26302a)"></div>
    <p class="col-lead">Lorem ipsum dolor sit amet, consectetuer adipiscing elit. Nam cursus.</p>
    <p class="col-body">Morbi ut mi. Nullam enim leo, egestas id, condimentum at, laoreet mattis, massa. Sed eleifend nonummy diam. Praesent mauris ante, elementum et, bibendum at, posuere sit amet, nibh. Duis tincidunt lectus quis dui viverra vestibulum.</p>
    <a class="btn abs" href="#" style="left:2px;top:228px">learn more ›</a>
  </section>

  <section class="abs col" style="left:472px">
    <div class="col-head" style="padding-left:7px">Recent Blog Post</div>
    <div class="post" style="top:40px"><h4>Tittle goes here</h4><p>Lorem ipsum dolor sit amet, consectetuer adipiscing elit. Nam cursus. Morbi ut mi. Nullam enim leo,</p><em>Posted on 23.08.2012</em></div>
    <div class="post" style="top:102px"><h4>Tittle goes here</h4><p>Lorem ipsum dolor sit amet, consectetuer adipiscing elit. Nam cursus. Morbi ut mi. Nullam enim leo,</p><em>Posted on 23.08.2012</em></div>
    <div class="post" style="top:164px"><h4>Tittle goes here</h4><p>Lorem ipsum dolor sit amet, consectetuer adipiscing elit. Nam cursus. Morbi ut mi. Nullam enim leo,</p><em>Posted on 23.08.2012</em></div>
    <a class="btn abs" href="#" style="left:1px;top:228px">view more ›</a>
  </section>

  <h2 class="abs brands-title">Our Brands Products</h2>

  <div class="abs card" style="left:37px;top:802px"><div class="shot" role="img" aria-label="Clear tequila bottle"></div><span>Product Name</span></div>
  <div class="abs card" style="left:161px;top:802px"><div class="shot" role="img" aria-label="Clear tequila bottle with gold label"></div><span>Product Name</span></div>
  <div class="abs card" style="left:286px;top:802px"><div class="shot" role="img" aria-label="Clear tequila bottle with blue label"></div><span>Product Name</span></div>
  <div class="abs card" style="left:410px;top:802px;height:149px"><div class="shot" role="img" aria-label="Clear tequila bottle with dark label"></div><span>Product Name</span></div>
  <div class="abs card" style="left:535px;top:802px"><div class="shot dark" role="img" aria-label="Black tequila bottle"></div><span>Product Name</span></div>

  <div class="abs card" style="left:37px;top:962px"><div class="shot" role="img" aria-label="Clear tequila bottle"></div><span>Product Name</span></div>
  <div class="abs card" style="left:160px;top:962px"><div class="shot" role="img" aria-label="Clear tequila bottle"></div><span>Product Name</span></div>
  <div class="abs card" style="left:286px;top:962px"><div class="shot" role="img" aria-label="Clear tequila bottle"></div><span>Product Name</span></div>
  <div class="abs card" style="left:411px;top:962px"><div class="shot" role="img" aria-label="Clear tequila bottle"></div><span>Product Name</span></div>
  <div class="abs card" style="left:535px;top:962px"><div class="shot" role="img" aria-label="Clear tequila bottle"></div><span>Product Name</span></div>

  <footer class="abs footer">
    <nav><a href="#">COMPANY</a><a href="#">ABOUT US</a><a href="#">PRODUCTS</a><a href="#">MANUFACTURE</a><a href="#">BRANDS</a><a href="#">BLOG</a><a href="#">OUR PLANT</a><a href="#">CONTACT</a></nav>
    <small>© 2012 Company Name &nbsp;|&nbsp; All right reserved &nbsp;|&nbsp; Term &amp; Conditions</small>
    <div class="social" aria-label="Social links"><i></i><i></i><i></i><i></i></div>
  </footer>
</div>
</body>
</html>
```